Geschäftspapiere für mobile Cocktailbar
Zielgruppe
Wir sind eine mobile Cocktailbar ! Wir arbeiten vielen Veranstaltungen / Festivals.
Ein sehr wichtiges Geschäftssegment sind Firmenveranstaltungen jeglicher Größe.
Hier stehen wir für sehr hohe Qualität an Service und an den Drinks.
Wir arbeiten stets mit Markenprodukten, professionellen Barkeepern und sehr hochwertigen Equipment
Unsere Website ist www.korbinel-bar.de
Aufgabenstellung
Es soll schlicht aber hochwertig sein
vielleicht eine Layout im Hintergrund
Drinks, Flüssigkeit, Bartending etc
Gerne auch das Logo eingebaut

```html
<!DOCTYPE html>
<html lang="de">
<head>
<meta charset="utf-8">
<title>Korbinel – Geschäftspapiere</title>
<link href="https://fonts.googleapis.com/css2?family=Montserrat:ital,wght@0,300;0,400;0,500;0,700;1,400;1,800&display=swap" rel="stylesheet">
<style>
  :root{
    --backdrop:#d6d6d6;
    --paper:#ffffff;
    --ink:#111111;
    --text:#2b2b2b;
    --header:#050608;
    --faint:#ececec;
    --photo-dark:#0b0c10;
    --photo-red:#7a1a1c;
  }
  *{margin:0;padding:0;box-sizing:border-box}
  html,body{width:1200px;height:864px;overflow:hidden;background:var(--backdrop);font-family:"Montserrat",sans-serif;color:var(--text)}
  .sheet{position:absolute;width:571px;height:807px;background:var(--paper);box-shadow:3px 4px 6px rgba(0,0,0,.25);overflow:hidden}
  .sheet--first{left:15px;top:27px}
  .sheet--follow{left:604px;top:37px}

  .header-band{position:absolute;left:0;top:0;width:571px;height:100px;background:var(--header)}
  .hero-photo{position:absolute;left:0;top:0;width:233px;height:276px;
    background:radial-gradient(ellipse at 40% 50%,var(--photo-red) 0%,#2a0c0e 30%,var(--photo-dark) 60%)}
  .brand{position:absolute;left:282px;top:31px;width:238px;text-align:center;color:var(--paper)}
  .brand-name{font-size:18px;font-weight:700;letter-spacing:6px;line-height:28px;padding-left:6px}
  .brand-url{margin-top:8px;font-size:6.5px;font-weight:700;letter-spacing:1.8px}

  .contact-list{position:absolute;left:284px;top:121px;list-style:none}
  .contact-list li{display:flex;align-items:center;height:21.7px;font-size:8.8px;color:var(--ink)}
  .contact-list svg{width:14px;height:14px;margin-right:19px}

  .subject{position:absolute;left:0;width:571px;top:322px;text-align:center;font-size:13.5px;font-weight:800;font-style:italic;letter-spacing:2.6px;color:var(--ink)}
  .lead{position:absolute;left:36px;top:370px;width:504px;text-align:center;font-size:12.4px;line-height:15px;font-style:italic;color:var(--ink)}
  .body-copy{position:absolute;left:33px;top:507px;width:510px;text-align:center;font-size:11.3px;line-height:13.8px;font-weight:300;color:var(--text)}

  .bar-motif{position:absolute;background:var(--faint);opacity:.6;border-radius:4px}
  .sheet--first .bar-motif{left:206px;top:634px;width:159px;height:108px}
  .sheet--follow .bar-motif{left:205px;top:623px;width:159px;height:117px}
  .signature-area{position:absolute;left:418px;top:634px;width:114px;height:90px;background:var(--faint);opacity:.5;border-radius:3px}

  .footer-rule{position:absolute;height:1.5px;background:var(--ink)}
  .sheet--first .footer-rule{left:41px;top:749px;width:488px}
  .sheet--follow .footer-rule{left:42px;top:749px;width:488px}
  .bank{position:absolute;left:0;width:556px;top:757px;text-align:center;font-size:8.6px;line-height:14.5px;font-weight:400;color:var(--ink)}
</style>
</head>
<body>
  <section class="sheet sheet--first">
    <div class="header-band"></div>
    <div class="hero-photo" role="img" aria-label="Foto eines roten Cocktails mit Strohhalm und Minze auf einer Schieferplatte vor schwarzem Hintergrund"></div>
    <div class="brand">
      <div class="brand-name">KORBINEL</div>
      <div class="brand-url">www.korbinel-crew.de</div>
    </div>

    <ul class="contact-list">
      <li><svg viewBox="0 0 14 14"><circle cx="7" cy="7" r="7" fill="#111"/><rect x="4.5" y="3.5" width="5" height="7" rx="1" fill="none" stroke="#fff" stroke-width="1.2"/></svg>Mobile Cocktailbar</li>
      <li><svg viewBox="0 0 14 14"><circle cx="7" cy="7" r="7" fill="#111"/><rect x="4" y="4" width="6" height="6" rx="1" fill="none" stroke="#fff" stroke-width="1.2"/><path d="M5.5 8.5l3-3" stroke="#fff" stroke-width="1.2"/></svg>Phone</li>
      <li><svg viewBox="0 0 14 14"><circle cx="7" cy="7" r="7" fill="#111"/><path d="M7 3.5a2 2 0 0 1 2 2c0 1.5-2 3.5-2 3.5s-2-2-2-3.5a2 2 0 0 1 2-2z" fill="none" stroke="#fff" stroke-width="1.1"/><path d="M4.5 10.5h5" stroke="#fff" stroke-width="1.1"/></svg>Location</li>
      <li><svg viewBox="0 0 14 14"><circle cx="7" cy="7" r="7" fill="#111"/><path d="M7 3.8l.9 2.2 2.3.2-1.8 1.5.6 2.3L7 8.8 5 10l.6-2.3-1.8-1.5 2.3-.2z" fill="#fff"/></svg>Address</li>
      <li><svg viewBox="0 0 14 14"><circle cx="7" cy="7" r="7" fill="#111"/><circle cx="7" cy="7" r="3.3" fill="none" stroke="#fff" stroke-width="1.2"/><path d="M5 9l4-4" stroke="#fff" stroke-width="1.2"/></svg>Website</li>
      <li><svg viewBox="0 0 14 14"><circle cx="7" cy="7" r="7" fill="#111"/><rect x="3.8" y="4.8" width="6.4" height="4.6" fill="#fff"/><path d="M3.8 4.8l3.2 2.5 3.2-2.5" fill="none" stroke="#111" stroke-width=".9"/></svg>Mail</li>
    </ul>

    <h1 class="subject">MOBILE COCKTAILBAR</h1>

    <p class="lead">Lorem ipsum dolor sit amet, consectetur adipiscing elit. Proin pretium neque at nibh ultricies, vel pretium risus volutpat. Fusce rhoncus, elit eu facilisis ultricies, velit leo pharetra sem, quis dignissim sapien lorem nec dui. Praesent dignissim tortor ante, quis venenatis ex tempus sed. Nulla turpis mauris, mollis non felis eu, egestas lobortis lectus. Nulla aliquet felis eget ullamcorper gravida. Nullam risus ipsum, sagittis vitae maximus quis, accumsan vel dolor. Curabitur metus quam,</p>

    <p class="body-copy">Lorem ipsum dolor sit amet, consectetur adipiscing elit. Proin pretium neque at nibh ultricies, vel pretium risus volutpat. Fusce rhoncus, elit eu facilisis ultricies, velit leo pharetra sem, quis dignissim sapien lorem nec dui. Praesent dignissim tortor ante, quis venenatis ex tempus sed. Nulla turpis mauris, mollis non felis eu, egestas lobortis lectus. Nulla aliquet felis eget ullamcorper gravida. Nullam risus ipsum, sagittis vitae maximus quis, accumsan vel dolor. Curabitur metus quam, semper id semper at, bibendum eget diam. Curabitur vitae luctus neque. Vestibulum rhoncus ac nisl vitae porttitor. Morbi fringilla varius mi at imperdiet. Vestibulum aliquet, justo sed commodo ultrices, nulla libero elementum urna, sit amet porta felis dolor eu purus.</p>

    <div class="bar-motif" role="img" aria-label="Blasse Strichzeichnung von Cocktailgläsern und Shaker als Hintergrundmotiv"></div>
    <div class="signature-area" role="img" aria-label="Handschriftliche Unterschrift"></div>

    <div class="footer-rule"></div>
    <div class="bank">Bank Details : 00-318207-40926735<br>Name of Bank</div>
  </section>

  <section class="sheet sheet--follow">
    <div class="bar-motif" role="img" aria-label="Blasse Strichzeichnung von Cocktailgläsern und Shaker als Hintergrundmotiv"></div>
    <div class="footer-rule"></div>
  </section>
</body>
</html>
```